Pipe Repair Clamps

A double side A4 showing our pipe repair clamps for stopping leaking pipes within seconds. For water , sewage companies, hotels, malls, airports, hosptals, facilities management companies and district cooling companies. Reverse side will show a size chart. Examples of product uploaded

```html
<!DOCTYPE html>
<html lang="en">
<head>
<meta charset="utf-8">
<title>Keystone Pipe Fittings – Pipe Repair Clamps Size Chart</title>
<link rel="stylesheet" href="https://fonts.googleapis.com/css2?family=Arimo:wght@400&family=Roboto:wght@400;500;700;900&display=swap">
<style>
  :root {
    --ink: #111111;
    --panel: #000000;
    --blue: #4f81c7;
    --orange: #d8802c;
    --logo-orange: #f29a32;
    --teal: #1fa6cb;
    --table-ink: #4a4a4a;
    --white: #ffffff;
  }
  * { margin: 0; padding: 0; box-sizing: border-box; }
  html, body { width: 927px; height: 1200px; overflow: hidden; }
  body { position: relative; font-family: "Roboto", sans-serif; color: var(--ink); }

  .backdrop {
    position: absolute; inset: 0;
    background: linear-gradient(180deg,
      #e6e8ec 0%, #e3e5ea 40%, #e6dfe0 62%, #e9d8d4 72%,
      #c9c3c3 80%, #b9b4ae 86%, #e4dcd6 90%, #ece6df 100%);
  }

  .size-chart {
    position: absolute; left: 70px; top: 54px; width: 545px;
    font-family: "Arimo", sans-serif; font-size: 10px; color: var(--table-ink);
  }
  .chart-row {
    display: grid;
    grid-template-columns: 58px 62px 58px 63px 57px 63px 57px 63px 1fr;
    height: 18.9px; align-items: center; white-space: nowrap;
  }
  .chart-head { height: 50px; align-items: center; line-height: 24px; }
  .chart-head .length { line-height: 12px; }
  .chart-codes { height: 22px; margin-bottom: 2px; }

  .side-panel {
    position: absolute; left: 624px; top: 0; width: 268px; height: 1096px;
    background: var(--panel);
  }
  .panel-foot {
    position: absolute; left: 624px; top: 1124px; width: 268px; height: 76px;
    background: var(--panel); border-top: 8px solid var(--orange);
  }
  .brand {
    position: absolute; left: 624px; top: 96px; width: 268px;
    display: flex; flex-direction: column; align-items: center; gap: 14px;
  }
  .brand-dot { width: 64px; height: 64px; border-radius: 50%; background: var(--logo-orange); }
  .brand-name {
    font-weight: 900; font-size: 24px; line-height: 28px; color: var(--logo-orange);
    text-align: center; text-transform: uppercase; letter-spacing: 1px;
  }

  .category {
    position: absolute; left: 622px; width: 272px; background: var(--blue);
    color: var(--white); font-weight: 700; font-size: 42px; line-height: 50px;
    display: flex; align-items: center; justify-content: center; text-align: center;
  }
  .category.capping { top: 304px; height: 78px; }
  .category.fittings { top: 390px; height: 88px; }
  .category.flow { top: 488px; height: 122px; }

  .about {
    position: absolute; left: 642px; top: 632px; width: 238px;
    color: var(--white); font-size: 17.4px; line-height: 21.8px;
  }
  .about p + p { margin-top: 21.8px; }

  .contact { position: absolute; left: 60px; width: 546px; text-align: center; }
  .contact-call { top: 1046px; font-size: 31px; font-weight: 500; color: var(--ink); }
  .contact-phone { top: 1076px; font-size: 78px; font-weight: 900; color: var(--orange); line-height: 84px; }
  .contact-web { top: 1150px; font-size: 19px; font-weight: 700; color: var(--teal); letter-spacing: 7px; }
</style>
</head>
<body>
  <div class="backdrop" role="img" aria-label="Photograph of a hazy city skyline with tall towers and waterfront villas under a soft sky"></div>

  <div class="size-chart">
    <div class="chart-row chart-head">
      <span>Pipe O.D.<br>Range(mm)</span><span>Working<br>pressure(bar)</span>
      <span>Pipe O.D.<br>Range(mm)</span><span>Working<br>pressure(bar)</span>
      <span>Pipe O.D.<br>Range(mm)</span><span>Working<br>pressure(bar)</span>
      <span>Pipe O.D.<br>Range(mm)</span><span>Working<br>pressure(bar)</span>
      <span class="length">Length(mm)</span>
    </div>
    <div class="chart-row chart-codes"><span>CR-1</span><span>PN</span><span>CR-2</span><span>PN</span><span>CR-3</span><span>PN</span><span>CR-4</span><span>PN</span><span>W</span></div>
    <div class="chart-row"><span>59-67</span><span>16</span><span></span><span></span><span></span><span></span><span></span><span></span><span>150-600</span></div>
    <div class="chart-row"><span>65-73</span><span>16</span><span></span><span></span><span></span><span></span><span></span><span></span><span>150-600</span></div>
    <div class="chart-row"><span>69-76</span><span>16</span><span></span><span></span><span></span><span></span><span></span><span></span><span>150-600</span></div>
    <div class="chart-row"><span>75-83</span><span>16</span><span></span><span></span><span></span><span></span><span></span><span></span><span>150-600</span></div>
    <div class="chart-row"><span>86-94</span><span>16</span><span>88-108</span><span>16</span><span></span><span></span><span></span><span></span><span>150-600</span></div>
    <div class="chart-row"><span>108-118</span><span>16</span><span>108-128</span><span>16</span><span></span><span></span><span></span><span></span><span>150-2000</span></div>
    <div class="chart-row"><span>113-121</span><span>16</span><span>113-133</span><span>16</span><span></span><span></span><span></span><span></span><span>150-2000</span></div>
    <div class="chart-row"><span>121-131</span><span>16</span><span>120-141</span><span>16</span><span></span><span></span><span></span><span></span><span>150-2000</span></div>
    <div class="chart-row"><span>126-136</span><span>16</span><span>168-188</span><span>16</span><span></span><span></span><span></span><span></span><span>150-2000</span></div>
    <div class="chart-row"><span>132-142</span><span>16</span><span>174-194</span><span>16</span><span></span><span></span><span></span><span></span><span>150-2000</span></div>
    <div class="chart-row"><span>145-155</span><span>16</span><span>219-239</span><span>16</span><span></span><span></span><span></span><span></span><span>150-2000</span></div>
    <div class="chart-row"><span>151-161</span><span>16</span><span>228-249</span><span>16</span><span></span><span></span><span></span><span></span><span>150-2000</span></div>
    <div class="chart-row"><span>159-170</span><span>16</span><span>238-258</span><span>16</span><span></span><span></span><span></span><span></span><span>150-2000</span></div>
    <div class="chart-row"><span>166-177</span><span>16</span><span>258-278</span><span>16</span><span></span><span></span><span></span><span></span><span>150-2000</span></div>
    <div class="chart-row"><span>170-180</span><span>16</span><span>273-293</span><span>16</span><span></span><span></span><span></span><span></span><span>150-2000</span></div>
    <div class="chart-row"><span>174-184</span><span>16</span><span>282-302</span><span>10</span><span></span><span></span><span></span><span></span><span>150-2000</span></div>
    <div class="chart-row"><span>179-189</span><span>16</span><span>295-315</span><span>10</span><span></span><span></span><span></span><span></span><span>150-2000</span></div>
    <div class="chart-row"><span>189-199</span><span>16</span><span>324-344</span><span>10</span><span></span><span></span><span></span><span></span><span>150-2000</span></div>
    <div class="chart-row"><span>218-228</span><span>16</span><span>335-356</span><span>10</span><span></span><span></span><span></span><span></span><span>150-2000</span></div>
    <div class="chart-row"><span>222-233</span><span>16</span><span>347-367</span><span>10</span><span></span><span></span><span></span><span></span><span>150-2000</span></div>
    <div class="chart-row"><span>229-239</span><span>16</span><span>357-376</span><span>10</span><span></span><span></span><span></span><span></span><span>150-2000</span></div>
    <div class="chart-row"><span>236-246</span><span>16</span><span>365-384</span><span>10</span><span></span><span></span><span></span><span></span><span>150-2000</span></div>
    <div class="chart-row"><span>248-258</span><span>16</span><span>383-402</span><span>10</span><span></span><span></span><span></span><span></span><span>150-2000</span></div>
    <div class="chart-row"><span>250-260</span><span>10</span><span>404-423</span><span>10</span><span></span><span></span><span></span><span></span><span>150-2000</span></div>
    <div class="chart-row"><span>252-263</span><span>10</span><span>421-440</span><span>10</span><span></span><span></span><span></span><span></span><span>150-2000</span></div>
    <div class="chart-row"><span>261-271</span><span>10</span><span>436-455</span><span>10</span><span></span><span></span><span></span><span></span><span>150-2000</span></div>
    <div class="chart-row"><span>271-281</span><span>10</span><span>453-472</span><span>10</span><span></span><span></span><span></span><span></span><span>150-2000</span></div>
    <div class="chart-row"><span>280-291</span><span>10</span><span>469-488</span><span>10</span><span></span><span></span><span></span><span></span><span>150-2000</span></div>
    <div class="chart-row"><span>288-298</span><span>10</span><span>488-507</span><span>10</span><span></span><span></span><span></span><span></span><span>150-2000</span></div>
    <div class="chart-row"><span>298-309</span><span>10</span><span>505-525</span><span>10</span><span></span><span></span><span></span><span></span><span>150-2000</span></div>
    <div class="chart-row"><span>300-310</span><span>10</span><span>526-545</span><span>8</span><span></span><span></span><span></span><span></span><span>150-2000</span></div>
    <div class="chart-row"><span>304-314</span><span>10</span><span>547-566</span><span>8</span><span></span><span></span><span></span><span></span><span>150-2000</span></div>
    <div class="chart-row"><span>321-331</span><span>10</span><span>562-581</span><span>8</span><span>630-660</span><span>8</span><span></span><span></span><span>150-2000</span></div>
    <div class="chart-row"><span>333-343</span><span>10</span><span>582-601</span><span>8</span><span>670-700</span><span>8</span><span></span><span></span><span>150-2000</span></div>
  </div>

  <aside class="side-panel"></aside>
  <div class="brand">
    <div class="brand-dot"></div>
    <div class="brand-name">Keystone<br>Pipe Fittings</div>
  </div>

  <div class="category capping">CAPPING</div>
  <div class="category fittings">FITTINGS</div>
  <div class="category flow">FLOW<br>CONTROL</div>

  <div class="about">
    <p>The company’s focus is on the civil engineering, water and sewerage treatment and gas industries, although some of the products offered are specifically for the building services and fire protection industries.</p>
    <p>We represent some of the world’s best-known manu-facturers and stock a full range of products at our premises in Carrowmore. All of our products are fully tested and approved to National and International standards and come with a full after sales service from both ourselves, and our suppliers.</p>
  </div>

  <div class="panel-foot"></div>

  <div class="contact contact-call">CALL US NOW</div>
  <div class="contact contact-phone">123 456 7890</div>
  <div class="contact contact-web">WWW.YOURWEBSITE.COM</div>
</body>
</html>
```